Vaporwyn Business Card

I need something that flows with the logo and looks professional but creative. I included the thumbnail file of the photo but will upload the source file once I have it. Colors of business card should flow. I am interested in doing the translucent clear plastic cards as well. My company is called Vaporwyn in one word and the contact details are below:

Dean Holloway
832-574-2938
www.VaporwynTx.example
dholloway_47@mailbox.example
Updates

Too much red. I'd rather focus on the blue and put some silver or grey in there.

New Files uploaded. Like the designs so far and am looking forward to seeing more.

Looking for a whole new direction. Let's forget about the plastic card. Let's focus on the blue more than red. I still haven't seen something that really grabs me.

Industry/Entity Type

Plastic

```html
<!DOCTYPE html>
<html lang="en">
<head>
<meta charset="utf-8">
<title>Vaporwyn Business Card</title>
<link rel="stylesheet" href="https://fonts.googleapis.com/css2?family=PT+Sans:ital,wght@0,400;0,700;1,400&display=swap">
<style>
  :root {
    --page-bg: #e9ebee;
    --card-frost-top: #f7f8f9;
    --card-frost-bottom: #e4e7ea;
    --card-edge: #cfd4d9;
    --blue-light: #2a8fc4;
    --blue-deep: #0f5b8a;
    --blue-logo: #1e7fc2;
    --frost-corner: #dfe4e8;
    --name-ink: #f4edd2;
    --detail-ink: #f2f5f8;
    --web-red: #e0262f;
  }
  * { box-sizing: border-box; margin: 0; padding: 0; }
  html, body {
    width: 1200px;
    height: 969px;
    overflow: hidden;
    background: var(--page-bg);
    font-family: "PT Sans", Arial, sans-serif;
  }
  .business-card {
    position: absolute;
    left: 120px;
    top: 220px;
    width: 960px;
    height: 530px;
    border-radius: 6px;
    overflow: hidden;
    background: linear-gradient(160deg, var(--card-frost-top), var(--card-frost-bottom));
    border: 1px solid var(--card-edge);
    box-shadow: 0 18px 40px rgba(20, 40, 60, 0.18);
  }
  .card-shapes {
    position: absolute;
    inset: 0;
    width: 100%;
    height: 100%;
  }
  .brand-name {
    position: absolute;
    left: 48px;
    top: 62px;
    display: flex;
    align-items: center;
    gap: 12px;
    font-size: 84px;
    font-weight: 400;
    color: var(--blue-logo);
    line-height: 1;
  }
  .brand-dot {
    width: 20px;
    height: 20px;
    border-radius: 50%;
    background: var(--blue-logo);
  }
  .person-name,
  .contact-line,
  .website {
    position: absolute;
    left: 511px;
    white-space: nowrap;
  }
  .person-name {
    top: 234px;
    font-size: 48px;
    font-style: italic;
    font-weight: 400;
    line-height: 58px;
    color: var(--name-ink);
  }
  .contact-line {
    display: flex;
    align-items: center;
    gap: 14px;
    font-size: 22px;
    line-height: 30px;
    color: var(--detail-ink);
  }
  .contact-line.phone { top: 322px; }
  .contact-line.email { top: 354px; }
  .contact-icon { width: 18px; height: 18px; flex: none; }
  .website {
    top: 398px;
    font-size: 24px;
    line-height: 30px;
    font-weight: 700;
    color: var(--web-red);
  }
</style>
</head>
<body>
  <div class="business-card">
    <svg class="card-shapes" viewBox="0 0 960 530" preserveAspectRatio="none" aria-hidden="true">
      <defs>
        <linearGradient id="blueBand" x1="0" y1="0" x2="1" y2="1">
          <stop offset="0" stop-color="var(--blue-light)"/>
          <stop offset="1" stop-color="var(--blue-deep)"/>
        </linearGradient>
      </defs>
      <polygon class="edge-sliver" points="0,0 16,0 60,530 0,530" fill="url(#blueBand)"/>
      <polygon class="main-band" points="549,0 960,0 960,256 836,530 309,530" fill="url(#blueBand)"/>
      <polygon class="frost-corner" points="960,256 960,530 836,530" fill="var(--frost-corner)"/>
    </svg>

    <div class="brand-name"><span>Vaporwyn</span><span class="brand-dot"></span></div>

    <p class="person-name">Dean Holloway</p>
    <p class="contact-line phone">
      <svg class="contact-icon" viewBox="0 0 20 20" aria-hidden="true">
        <path d="M5 2l3 4-2 2c1 2.5 3.5 5 6 6l2-2 4 3-2 3C9 18 2 11 2 4z" fill="currentColor"/>
      </svg>
      <span>832-574-2938</span>
    </p>
    <p class="contact-line email">
      <svg class="contact-icon" viewBox="0 0 20 20" aria-hidden="true">
        <rect x="1.5" y="4" width="17" height="12" rx="1.5" fill="currentColor"/>
        <path d="M2 5l8 6 8-6" fill="none" stroke="var(--blue-deep)" stroke-width="1.5"/>
      </svg>
      <span>dholloway_47@mailbox.example</span>
    </p>
    <p class="website">www.VaporwynTx.example</p>
  </div>
</body>
</html>
```